Martial art rank diploma

Need a diploma for a martial arts belt rank . The art is Japanese in origin , traditional is good , stylish , eye catching .
Dragons are good , no cartoon figures . Tacky is not good . Something proud to display
No martial art poses
Must have place for date , head instructor signature

And must say (a blank for students name )
"Having confirmed with all standards and requirements set forth by Brantwell Martial Arts and Fitness , is hereby promoted to the rank of " ( a blank for the rank)
Updates

Reason: nice designs, need to see more to compare

Industry/Entity Type

Martial Art

Requirements
Must have
• Logo attached and name of the school
Nice to have
• Dragon , that does not look like a centipede .

maybe best to have a dragon in the background as a water mark type of thing.
Should not have
• Tacky look or cartoon figures, or any martial art poses

```html
<!DOCTYPE html>
<html lang="en">
<head>
<meta charset="utf-8">
<title>Belt Rank Diploma – Brantwell Martial Arts and Fitness</title>
<link rel="stylesheet" href="https://fonts.googleapis.com/css2?family=Jockey+One&family=Russo+One&family=Arimo:wght@400&family=Rubik:ital,wght@1,500&display=swap">
<style>
  :root {
    --page-bg: #ececec;
    --panel-light: #f3f3f2;
    --panel-dark: #e2e0dd;
    --band-grey: #a9a9a9;
    --orange-deep: #e8532a;
    --orange-mid: #ee6a37;
    --orange-soft: #f07d4d;
    --white: #ffffff;
    --ink-grey: #555353;
    --label-orange: #e9552b;
  }
  * { margin: 0; padding: 0; box-sizing: border-box; }
  html, body { width: 1200px; height: 1000px; overflow: hidden; }
  body { background: var(--page-bg); position: relative; }

  .diploma {
    position: absolute;
    left: 78px; top: 93px;
    width: 1030px; height: 794px;
    background: linear-gradient(180deg, var(--panel-dark), var(--panel-light));
    overflow: hidden;
  }
  .diploma__field { position: absolute; inset: 0; }

  .school-name {
    position: absolute;
    left: 14px; top: 340px;
    width: 280px;
    display: flex; align-items: center; gap: 10px;
    font-family: "Russo One", sans-serif;
    color: var(--ink-grey);
    font-size: 24px; line-height: 1.1;
  }
  .school-name__dot {
    flex: none; width: 44px; height: 44px;
    border-radius: 50%;
    background: var(--label-orange);
  }
  .crest-art {
    position: absolute;
    left: 104px; top: 422px;
    width: 94px; height: 105px;
    border-radius: 8px;
    background: radial-gradient(circle, #8a7f7f 0%, #c4bfbd 70%, transparent 100%);
  }

  .title {
    position: absolute;
    left: 300px; top: 98px;
    width: 720px;
    text-align: center;
    white-space: nowrap;
    font-family: "Jockey One", sans-serif;
    font-weight: 400;
    font-size: 74px; line-height: 1;
    letter-spacing: 3px;
    color: var(--white);
    transform: skewX(-10deg);
  }

  .blank {
    position: absolute;
    background: var(--white);
    border-radius: 34px;
  }
  .blank__label {
    position: absolute; left: 0; right: 0; bottom: 3px;
    text-align: center;
    font-family: "Rubik", sans-serif;
    font-style: italic; font-weight: 500;
    font-size: 15px;
    color: var(--label-orange);
  }
  .blank--student { left: 355px; top: 245px; width: 602px; height: 112px; border-radius: 46px; }
  .blank--rank { left: 489px; top: 443px; width: 351px; height: 96px; border-radius: 28px; }
  .blank--date { left: 291px; top: 683px; width: 296px; height: 77px; border-radius: 26px; }
  .blank--date .blank__label { bottom: -2px; }
  .blank--instructor { left: 689px; top: 682px; width: 296px; height: 76px; border-radius: 26px; }

  .promotion-text {
    position: absolute;
    left: 318px; top: 376px;
    width: 698px;
    text-align: center;
    font-family: "Arimo", sans-serif;
    font-size: 21px; line-height: 18px;
    color: var(--white);
  }
</style>
</head>
<body>
  <main class="diploma">
    <svg class="diploma__field" viewBox="0 0 1030 794" role="img" aria-label="Orange field with a faint dragon watermark in the background">
      <defs>
        <linearGradient id="orange-field" x1="0" y1="0" x2="0" y2="1">
          <stop offset="0" stop-color="#e8532a"/>
          <stop offset="0.5" stop-color="#ee6a37"/>
          <stop offset="1" stop-color="#f07d4d"/>
        </linearGradient>
        <radialGradient id="watermark-glow" cx="0.6" cy="0.55" r="0.5">
          <stop offset="0" stop-color="#f6915f" stop-opacity="0.45"/>
          <stop offset="1" stop-color="#f6915f" stop-opacity="0"/>
        </radialGradient>
      </defs>
      <path d="M198,0 Q430,397 198,794 L1030,794 L1030,0 Z" fill="#a9a9a9"/>
      <path d="M216,0 Q446,397 216,794 L1030,794 L1030,0 Z" fill="url(#orange-field)"/>
      <path d="M216,0 Q446,397 216,794 L1030,794 L1030,0 Z" fill="url(#watermark-glow)"/>
    </svg>

    <div class="school-name">
      <span class="school-name__dot"></span>
      <span>Brantwell Martial Arts &amp; Fitness</span>
    </div>
    <div class="crest-art" role="img" aria-label="Small grey dragon emblem"></div>

    <h1 class="title">BELT RANK DIPLOMA</h1>

    <div class="blank blank--student"><span class="blank__label">Student Name</span></div>

    <p class="promotion-text">Having confirmed with all standards and requirements set forth<br>by Brantwell Martial Arts and Fitness , is hereby promoted to the<br>rank of</p>

    <div class="blank blank--rank"><span class="blank__label">Rank</span></div>
    <div class="blank blank--date"><span class="blank__label">Date</span></div>
    <div class="blank blank--instructor"><span class="blank__label">Head Instructor</span></div>
  </main>
</body>
</html>
```